Softwareentwickler sucht Disigne für Flyer
Zielgruppe
Softwareentwicklung im Bereich Feuerwehr und Rettungsdienst.
Aufgabenstellung
Ich benötige für unsere Software ein Flyer für ein Messeauftritt. Wir haben eine Homepage (www.norvaplex.de) ,wo unsere Software beschrieben wird. Es besteht bereits ein Softwarelogo (q.-Lager+) welches auch auf unserer Hompage zu sehen ist.

```html
<!DOCTYPE html>
<html lang="de">
<head>
<meta charset="utf-8">
<title>norvaplex Flyer</title>
<link href="https://fonts.googleapis.com/css2?family=Mulish:wght@700;800&family=Questrial&display=swap" rel="stylesheet">
<style>
  :root {
    --orange: #f9b043;
    --ink: #222222;
    --line: #b8b8b8;
    --blue-light: #0b63ad;
    --blue-mid: #0b3f8a;
    --blue-deep: #0a0b4a;
    --tick: #f9b043;
    --white: #ffffff;
  }
  * { margin: 0; padding: 0; box-sizing: border-box; }
  html, body { width: 1140px; height: 1200px; overflow: hidden; background: var(--white); }
  body { position: relative; font-family: "Questrial", sans-serif; color: var(--white); }

  .sheet { position: absolute; left: 166px; width: 808px; height: 543px; border: 1px solid var(--line); background: var(--white); overflow: hidden; }
  .sheet--outside { top: 37px; }
  .sheet--inside { top: 619px; }

  .band { position: absolute; left: 0; width: 100%; background: var(--orange); }
  .band--top { top: 0; height: 63px; }
  .band--bottom { bottom: 0; height: 61px; }
  .rule { position: absolute; left: 0; width: 100%; height: 5px; background: var(--ink); }
  .rule--top { top: 63px; }
  .rule--bottom { top: 477px; }

  .header { position: absolute; top: 68px; left: 0; width: 100%; height: 65px; }
  .fold { position: absolute; top: 0; width: 1px; height: 100%; background: var(--line); }

  .panel-title { position: absolute; top: 0; height: 65px; display: flex; align-items: center; justify-content: center; font-family: "Mulish", sans-serif; font-weight: 800; color: var(--ink); font-size: 19px; white-space: nowrap; }
  .welcome-title { left: 16px; width: 252px; justify-content: flex-start; font-size: 17.5px; }
  .claim-title { left: 271px; width: 271px; font-size: 17.5px; }

  .field { position: absolute; top: 133px; left: 0; width: 100%; height: 344px; }
  .field--outside { background: linear-gradient(90deg, var(--blue-light) 0%, var(--blue-mid) 45%, var(--blue-deep) 100%); }
  .field--inside { background: radial-gradient(ellipse at 50% 45%, #2f6fd0 0%, #1450a8 35%, var(--blue-mid) 65%, var(--blue-deep) 100%); }

  .features { position: absolute; top: 151px; left: 16px; width: 250px; list-style: none; font-size: 10px; line-height: 13.6px; }
  .features li { position: relative; padding-left: 16px; white-space: nowrap; }
  .features li::before { content: "\2713"; position: absolute; left: 0; color: var(--tick); font-size: 9px; }

  .contact { position: absolute; left: 288px; top: 150px; font-size: 10px; line-height: 11px; }
  .contact .company { font-family: "Mulish", sans-serif; font-weight: 700; font-size: 10px; margin-bottom: 21px; }
  .contact p { margin-bottom: 11px; }

  .claim { position: absolute; left: 547px; width: 260px; top: 168px; text-align: center; font-family: "Mulish", sans-serif; font-weight: 700; font-size: 15px; line-height: 18px; }

  .brand { position: absolute; top: 0; height: 65px; display: flex; align-items: center; justify-content: center; gap: 8px; font-family: "Mulish", sans-serif; font-weight: 800; color: var(--ink); }
  .brand--company { left: 537px; width: 271px; font-size: 24px; letter-spacing: 1px; }
  .brand--company .mark { width: 12px; height: 12px; background: var(--orange); }
  .brand--product { left: 542px; width: 266px; font-size: 24px; }

  .photo-arc { position: absolute; top: 133px; left: 0; width: 808px; height: 344px; }
  .photo-ring { position: absolute; left: 324px; top: 168px; width: 164px; height: 164px; border-radius: 50%; border: 6px solid var(--orange); background: linear-gradient(135deg, #d8dde6 0%, #8fa6c4 45%, #4f6f99 100%); }

  .copy { position: absolute; font-size: 10px; line-height: 10.9px; white-space: nowrap; }
  .copy--welcome { left: 16px; top: 152px; width: 252px; }
  .copy--welcome p + p { margin-top: 21px; }
  .copy--product { left: 562px; top: 155px; width: 240px; }
  .copy--product h3 { font-family: "Mulish", sans-serif; font-weight: 700; font-size: 9.8px; line-height: 12px; margin-bottom: 10px; }
  .copy--product p { margin-bottom: 11px; }
  .copy--product h3.spaced { margin-top: 14px; }
</style>
</head>
<body>

<section class="sheet sheet--outside">
  <div class="band band--top" role="img" aria-label="Orangefarbenes Streifenband"></div>
  <div class="rule rule--top"></div>
  <header class="header">
    <div class="fold" style="left:266px"></div>
    <div class="fold" style="left:537px"></div>
    <h2 class="panel-title" style="left:0;width:266px">Funktionen</h2>
    <h2 class="panel-title" style="left:266px;width:271px">Kontakt</h2>
    <div class="brand brand--company"><span class="mark"></span>NORVAPLEX</div>
  </header>
  <div class="field field--outside"></div>

  <svg class="photo-arc" viewBox="0 0 808 344">
    <defs>
      <linearGradient id="photoTone" x1="0" y1="0" x2="1" y2="0">
        <stop offset="0" stop-color="#e4e5ea"/>
        <stop offset="0.4" stop-color="#9c9ea8"/>
        <stop offset="0.55" stop-color="#b9aaa4"/>
        <stop offset="0.8" stop-color="#6f8fb4"/>
        <stop offset="1" stop-color="#a59a98"/>
      </linearGradient>
    </defs>
    <circle cx="576" cy="451" r="318" fill="url(#photoTone)" stroke="#f9b043" stroke-width="8" role="img" aria-label="Foto: Handscanner auf heller Fläche und Nahaufnahme eines Auges"/>
  </svg>

  <ul class="features">
    <li>Steuerung von Benutzerkonten</li>
    <li>Verwaltung von Lieferanten und Lagerstandorte</li>
    <li>Steuerung von einzelnen Standorten (Mandan<br>ten) und oder Zentrallager</li>
    <li>Standortüberwachung (mit E-Mailbe-<br>nachrichtigung)</li>
    <li>Artikelverwaltung</li>
    <li>Mindesthaltbarkeitskontrolle</li>
    <li>Temperaturüberwachung von Medizinischen<br>Kühlschränken</li>
    <li>Scanaktivitätsübersicht</li>
    <li>Live Streaming von Scanaktivität über Monitor<br>in Ihrem Lager</li>
    <li>Komplettes Bestellwesen inkl. Ein<br>lagerungsmöglichkeit</li>
    <li>Inventur und Artikelstatistiken auf Knopfdruck</li>
    <li>Hoher Schutz durch SSL (Secure Sockets Layer)</li>
    <li>Bestellstatistiken</li>
    <li>MPG Verwaltung</li>
    <li>SMS-Alarm bei Unregelmäßigkeiten wie<br>z.B. Temperaturabweichungen</li>
    <li>Neu: Modul Fuhrpark</li>
  </ul>

  <div class="contact">
    <p class="company">norvaplex</p>
    <p>Lindenweg 14<br>65510 Idstein<br>Telefon: +49 6120 448210</p>
    <p>Geschäftsführer: Jonas Keller</p>
    <p>E-Mail: info@norvaplex.de<br>Internet: www.norvaplex.de</p>
  </div>

  <h1 class="claim">Ihr Experte für Lagerverwaltung<br>mit Barcodescannern und<br>Erfassungssystemen</h1>

  <div class="rule rule--bottom"></div>
  <div class="band band--bottom" role="img" aria-label="Orangefarbenes Streifenband"></div>
</section>

<section class="sheet sheet--inside">
  <div class="band band--top" role="img" aria-label="Orangefarbenes Streifenband"></div>
  <div class="rule rule--top"></div>
  <header class="header">
    <div class="fold" style="left:271px"></div>
    <div class="fold" style="left:542px"></div>
    <h2 class="panel-title welcome-title">Willkommen bei norvaplex,</h2>
    <h2 class="panel-title claim-title">Wir haben ein Auge drauf</h2>
    <div class="brand brand--product">q.-Lager+</div>
  </header>
  <div class="field field--inside" role="img" aria-label="Illustration: Leiterbahnen mit Symbolen für Einkauf, Preisschild und Rechner auf blauem Grund"></div>
  <div class="photo-ring" role="img" aria-label="Foto: Nahaufnahme eines Auges hinter Strichmuster"></div>

  <div class="copy copy--welcome">
    <p>Ihrem Innovativen Partner für Lagerlösungen<br>in medizinischen Bereichen.<br>Von der EDV gestützten Lagerverwaltung bis hin zur<br>vollständigen Überwachung von<br>Temperaturen, bietet Ihnen unser Unternehmen eine<br>Vielzahl an individuellen Produkten und<br>Lösungen an.<br>Vertrauen Sie unserer Kompetenz und vereinbaren<br>Sie ein unverbindliches Beratungsgespräch mit Uns!<br>Unsere Aufgabe ist unser Motto.<br>Deshalb bieten wir dem Lager eine Technik von<br>größter Sorgfalt und neuen Ideen.</p>
    <p>Als Experten für Identifikationslösungen wissen wir von<br>norvaplex, wie wir Ihre Lagerverwaltung am effek-<br>tivsten mit Barcodescannern und Erfassungssystemen<br>ausstatten. Nach einer umfangreichen Analyse und<br>Beratungsphase planen wir die Installation Ihres neuen<br>Verwaltungssystems mit Ihnen gemeinsam. Denn jede<br>Erfassungslösung kann unterschiedlich ausfallen und<br>schließlich wollen wir das System optimal an Ihr Un-<br>ternehmen anpassen - nicht umgekehrt.</p>
  </div>

  <div class="copy copy--product">
    <h3>Lagerverwaltung einfach Online mit q.-Lager+</h3>
    <p>Wir von norvaplex haben es uns zur Aufgabe<br>gemacht, die Lagerverwaltung in verschiedenen<br>Bereichen zu erleichtern und zu steuern.</p>
    <p>Die gesamte Steuerung des Client-Systems wird<br>über die Anbindung eines Handscanners (Barcode-<br>Scanner) realisiert. Angefangen von der einfachen<br>Lagerverwaltung wie z.B. dass Ein- und Auslagern<br>von Waren bis hin zur Überwachung von Küh-<br>lschranktemperaturen und Haltbarkeitsdaten.</p>
    <h3 class="spaced">In der Lagerverwaltung<br>Barcode-Systeme einsetzen</h3>
    <p>Zur übersichtlicheren Erfassung von Waren in der<br>Lagerverwaltung können Barcode-Systeme eine<br>erhebliche Erleichterung darstellen. Nur zu oft kann<br>es in der Warenverwaltung im Lager zu Verwirrun-<br>gen kommen. Durch eine Vielzahl von Lagerplätzen<br>kann die Erfassung der Waren leicht durcheinander<br>geraten und fehlerhaft weitergegeben werden.<br>Um diese Prozesse für Ihre Mitarbeiter einfacher<br>zu gestalten, können Sie in Ihrer Lagerverwaltung<br>Barcode-Systeme einsetzen.</p>
  </div>

  <div class="rule rule--bottom"></div>
  <div class="band band--bottom" role="img" aria-label="Orangefarbenes Streifenband"></div>
</section>

</body>
</html>
```